Redesign of an existing homepage

This site needs a redesign
https://www.weiler-am-kornfeld.de
This page with the accommodation options is important for the customer
https://www.weiler-am-kornfeld.de/gastgeber/
Till now there is a new logo. See attachment. That's all I have.
It would make sense to use the colors of the logo in the redesign.
footer.jpg.
I would put this info into the footer. The graphic (Infomaterial) is not needed.
a new menu - links.jpg
This info can be put in a new menu. Therefore the right column is gone and there is more space for the design.
NEW:
Please keep in mind that the Icons are important and shall be displayed under every accommodation

```html
<!DOCTYPE html>
<html lang="de">
<head>
<meta charset="utf-8">
<title>Tourismusverband Weiler am Kornfeld</title>
<link rel="stylesheet" href="https://fonts.googleapis.com/css2?family=Raleway:wght@300;700&family=Roboto:wght@400;500&display=swap">
<style>
  :root {
    --blue: #1a6fb5;
    --sky: #bfe5f5;
    --green: #7ab51d;
    --ink: #111111;
    --grey-text: #444444;
    --placeholder: #c7c7c7;
    --white: #ffffff;
  }
  * { margin: 0; padding: 0; box-sizing: border-box; }
  html, body { width: 1200px; height: 780px; overflow: hidden; background: var(--white); }
  body { position: relative; font-family: "Roboto", Arial, sans-serif; }
  .hero-bg { position: absolute; left: 0; top: 0; width: 1200px; height: 780px; z-index: 0; }
  .site-header { position: absolute; top: 0; left: 0; width: 1200px; height: 110px; z-index: 2; }
  .brand { position: absolute; left: 186px; top: 22px; display: flex; flex-direction: column; align-items: center; width: 124px; }
  .brand-mark { width: 42px; height: 42px; border-radius: 50%; background: var(--blue); margin-bottom: 6px; }
  .brand-name { font-family: "Roboto", Arial, sans-serif; font-weight: 500; font-size: 10.5px; line-height: 13px; color: var(--blue); text-align: center; }
  .main-nav { position: absolute; left: 425px; top: 65px; display: flex; gap: 14px; }
  .main-nav a { color: var(--blue); text-decoration: none; font-size: 14.5px; font-weight: 400; }
  .hero { position: absolute; top: 160px; left: 0; width: 1200px; text-align: center; z-index: 2; }
  .hero-title { font-family: "Raleway", sans-serif; font-weight: 300; font-size: 33px; color: var(--ink); letter-spacing: 0.2px; }
  .hero-tagline { margin-top: 18px; font-family: "Raleway", sans-serif; font-weight: 700; font-size: 25px; color: var(--ink); }
  .hero-tagline .marked { position: relative; display: inline-block; }
  .hero-tagline .marked svg { position: absolute; left: 6px; bottom: -14px; }
  .hero-media { position: absolute; left: 283px; top: 325px; width: 634px; height: 274px; background: var(--placeholder); z-index: 2; }
  .features { position: absolute; top: 700px; left: 0; width: 1200px; z-index: 2; }
  .feature { position: absolute; width: 240px; text-align: center; }
  .feature svg { display: block; margin: 0 auto; }
  .feature-title { margin-top: 18px; font-family: "Roboto", Arial, sans-serif; font-weight: 500; font-size: 22px; color: var(--blue); }
</style>
</head>
<body>
  <svg class="hero-bg" viewBox="0 0 1200 780" aria-hidden="true">
    <defs>
      <linearGradient id="sky" x1="0" y1="0" x2="0" y2="1">
        <stop offset="0.15" stop-color="#ffffff"/>
        <stop offset="1" stop-color="#bfe5f5"/>
      </linearGradient>
    </defs>
    <path d="M0 0 H1200 V377 Q600 740 0 377 Z" fill="url(#sky)"/>
  </svg>

  <header class="site-header">
    <div class="brand">
      <span class="brand-mark"></span>
      <span class="brand-name">Tourismusverband<br>Weiler am Kornfeld</span>
    </div>
    <nav class="main-nav">
      <a href="https://www.weiler-am-kornfeld.de">Home</a>
      <a href="#">Kornfeldtal</a>
      <a href="https://www.weiler-am-kornfeld.de/gastgeber/">Gastgeber</a>
      <a href="#">Freizeit</a>
      <a href="#">Ausflugsziele</a>
      <a href="#">Kunst und Kultur</a>
      <a href="#">Kontakt/Datenschutz</a>
    </nav>
  </header>

  <section class="hero">
    <h1 class="hero-title">Fremdenverkehrsverein Weiler am Kornfeld und Umgebung</h1>
    <p class="hero-tagline">einfach nur <span class="marked">gast sein<svg width="96" height="10" viewBox="0 0 96 10" aria-hidden="true"><path d="M2 7 Q40 3 94 2" stroke="var(--green)" stroke-width="4" fill="none" stroke-linecap="round"/></svg></span>.</p>
  </section>

  <div class="hero-media" role="img" aria-label="Bild oder Video der Region"></div>

  <section class="features">
    <div class="feature" style="left:206px">
      <svg width="40" height="40" viewBox="0 0 40 40" aria-hidden="true">
        <circle cx="20" cy="20" r="17" fill="#f6dfa8"/>
        <rect x="11" y="11" width="18" height="18" rx="3" fill="#f3c9b0" stroke="#c0392b" stroke-width="2"/>
        <circle cx="20" cy="20" r="5" fill="none" stroke="#c0392b" stroke-width="1.5"/>
        <path d="M20 20 L22 17" stroke="#c0392b" stroke-width="1.5"/>
      </svg>
      <h2 class="feature-title">Veranstaltungen</h2>
    </div>
    <div class="feature" style="left:480px">
      <svg width="40" height="40" viewBox="0 0 40 40" aria-hidden="true">
        <circle cx="20" cy="20" r="17" fill="#f6dfa8"/>
        <circle cx="20" cy="20" r="10" fill="#6a9fd8" stroke="#2f5f9e" stroke-width="1.5"/>
        <rect x="19" y="18" width="2" height="7" fill="#fff"/>
        <circle cx="20" cy="15.5" r="1.3" fill="#fff"/>
      </svg>
      <h2 class="feature-title">Infomaterial</h2>
    </div>
    <div class="feature" style="left:754px">
      <svg width="40" height="40" viewBox="0 0 40 40" aria-hidden="true">
        <circle cx="20" cy="20" r="17" fill="#f6dfa8"/>
        <rect x="11" y="11" width="18" height="18" rx="3" fill="#b7a9d6" stroke="#4a3f6b" stroke-width="1.5"/>
        <path d="M15 25 L16 22 L25 13 L27 15 L18 24 Z" fill="#fff" stroke="#4a3f6b" stroke-width="1"/>
      </svg>
      <h2 class="feature-title">Weiler am Kornfeld</h2>
    </div>
  </section>
</body>
</html>
```